You’re Cordially Invited
To a Sunset Celebration Honoring the Launch of The Calloway

Date: Thursday, May 15
Time: 5:30 PM – 7:30 PM
Location: The Calloway, 47 Marlow Lane, East Boston

Please join us for an elegant evening of connection and celebration as we unveil The Calloway Project.
Enjoy private tours of Units 3 and 4, along with our breathtaking roof deck offering sweeping views of East Boston at sunset.

Sip curated selections of beer and wine and savor light seasonal bites as you mingle with colleagues and guests.

Feel free to bring clients, friends, or family — all are welcome!

Kindly RSVP to:
Daria Whitfield, Sparrowgate Realty
📧 Daria@sparrowgatehomes.example

Please include logo, classic design, and attachments. Colors navy, gold, white

```html
<!DOCTYPE html>
<html lang="en">
<head>
<meta charset="utf-8">
<title>Sunset Celebration – The Calloway</title>
<link rel="stylesheet" href="https://fonts.googleapis.com/css2?family=Cinzel:wght@400;600;700&family=Montserrat:wght@300;400;700&display=swap">
<style>
  :root {
    --navy: #23345a;
    --navy-light: #2b3d66;
    --navy-deep: #1f2e50;
    --gold: #d6b063;
    --gold-light: #ecd08c;
    --gold-dark: #b98d3c;
    --white: #f2f2f2;
  }
  * { margin: 0; padding: 0; box-sizing: border-box; }
  html, body { width: 1200px; height: 2215px; overflow: hidden; background: var(--navy); }
  .invitation {
    position: relative;
    width: 1200px;
    height: 2215px;
    background: var(--navy);
    color: var(--white);
    font-family: "Montserrat", sans-serif;
    font-weight: 300;
  }
  .hero-art, .frame { position: absolute; left: 0; top: 0; }
  .line {
    position: absolute;
    left: 0;
    right: 0;
    text-align: center;
    white-space: nowrap;
  }
  .gold-text {
    background: linear-gradient(180deg, var(--gold-light) 0%, var(--gold) 50%, var(--gold-dark) 100%);
    -webkit-background-clip: text;
    background-clip: text;
    color: transparent;
  }
  .brand-mark {
    position: absolute;
    left: 550px; top: 153px;
    width: 100px; height: 100px;
    border: 4px solid var(--gold);
    border-radius: 50%;
  }
  .brand-name {
    top: 278px;
    font-family: "Cinzel", serif;
    font-weight: 600;
    font-size: 36px;
    line-height: 48px;
    letter-spacing: 0.02em;
    color: var(--gold);
  }
  .invited {
    top: 408px;
    font-family: "Montserrat", sans-serif;
    font-weight: 400;
    font-size: 33px;
    line-height: 44px;
    letter-spacing: 0.3em;
    padding-left: 0.3em;
  }
  .title { font-family: "Cinzel", serif; font-weight: 400; }
  .title-lead {
    left: 304px; right: auto;
    top: 563px;
    font-size: 30px;
    line-height: 36px;
  }
  .title-sunset { top: 552px; font-size: 112px; line-height: 124px; }
  .title-celebration { top: 700px; font-size: 114px; line-height: 126px; }
  .honoring {
    font-family: "Cinzel", serif;
    font-weight: 700;
    font-size: 40px;
    line-height: 50px;
    letter-spacing: 0.05em;
  }
  .honoring-1 { top: 873px; }
  .honoring-2 { top: 934px; }
  .event-date { top: 1120px; font-size: 64px; line-height: 76px; font-weight: 300; }
  .event-time { top: 1218px; font-size: 29px; line-height: 40px; }
  .event-place { font-size: 30px; line-height: 42px; }
  .event-place-1 { top: 1285px; }
  .event-place-2 { top: 1333px; }
  .message {
    position: absolute;
    left: 140px;
    width: 920px;
    font-size: 23px;
    line-height: 38px;
    text-align: justify;
    text-align-last: center;
  }
  .message-1 { top: 1500px; }
  .message-2 { top: 1657px; }
  .welcome {
    font-family: "Cinzel", serif;
    font-size: 30px;
    line-height: 44px;
    color: var(--gold);
  }
  .welcome-1 { top: 1772px; }
  .welcome-2 { top: 1820px; }
  .rsvp { font-size: 25px; line-height: 38px; }
  .rsvp-label { top: 1987px; }
  .rsvp-name { top: 2029px; }
  .rsvp-name strong { font-weight: 700; color: var(--gold); }
  .rsvp-email { top: 2104px; }
</style>
</head>
<body>
<main class="invitation">
  <svg class="hero-art" width="1200" height="1200" role="img" aria-label="Faint illustration of a historic row-house street facade behind the heading">
    <defs>
      <linearGradient id="heroShade" x1="0" y1="0" x2="0" y2="1">
        <stop offset="0" stop-color="#2a3c64"/>
        <stop offset="1" stop-color="#24365c"/>
      </linearGradient>
    </defs>
    <path d="M0 0 H1200 V880 Q600 1180 0 880 Z" fill="url(#heroShade)"/>
  </svg>

  <svg class="frame" width="1200" height="2215" aria-hidden="true">
    <g stroke="#d6b063" stroke-width="2.5" fill="none">
      <path d="M363 2125 H62 V88 H1138 V2125 H834"/>
    </g>
  </svg>

  <div class="brand-mark" aria-hidden="true"></div>
  <p class="line brand-name">SPARROWGATE REALTY</p>

  <p class="line invited">YOU’RE CORDIALLY INVITED</p>

  <h1>
    <span class="line title title-lead gold-text">TO A</span>
    <span class="line title title-sunset gold-text">SUNSET</span>
    <span class="line title title-celebration gold-text">CELEBRATION</span>
  </h1>
  <h2>
    <span class="line honoring honoring-1 gold-text">HONORING THE LAUNCH OF</span>
    <span class="line honoring honoring-2 gold-text">THE CALLOWAY</span>
  </h2>

  <p class="line event-date">THURSDAY, MAY 15</p>
  <p class="line event-time">Time: 5:30 PM – 7:30 PM</p>
  <p class="line event-place event-place-1">Location: The Calloway,</p>
  <p class="line event-place event-place-2">47 Marlow Lane, East Boston</p>

  <p class="message message-1">Please join us for an elegant evening of connection and celebration as we unveil The Calloway Project. Enjoy private tours of Units 3 and 4, along with our breathtaking roof deck offering sweeping views of East Boston at sunset.</p>
  <p class="message message-2">Sip curated selections of beer and wine and savor light seasonal bites as you mingle with colleagues and guests.</p>

  <p class="line welcome welcome-1">Feel free to bring clients, friends, or family -</p>
  <p class="line welcome welcome-2">all are welcome!</p>

  <p class="line rsvp rsvp-label">Kindly RSVP to:</p>
  <p class="line rsvp rsvp-name"><strong>DARIA WHITFIELD,</strong> Sparrowgate Realty</p>
  <p class="line rsvp rsvp-email">Daria@sparrowgatehomes.example</p>
</main>
</body>
</html>
```